Honey Jar Label Design

I am looking for a fun label design for a 1 lb honey jar.
The company is Corliss Waverly Botanicals, which sells cut flowers and is expanding into honey and eventually other honey products. I've included the design work for the business, and I'd like the honey products to coordinate with them but not necessarily match directly.
Label requirements:
Raw Honey
Corliss Waverly Botanicals
27308 Quarry Bend Rd
Alderbrook, MO 66341
NET WT. 16 OZ. (weight info must be in the lower third of the front label and easy to read)
Look and feel
Each slider illustrates characteristics of the customer's brand and the style your logo design should communicate.

```html
<!DOCTYPE html>
<html lang="en">
<head>
<meta charset="utf-8">
<title>Corliss Waverly Botanicals – Raw Honey Label</title>
<link href="https://fonts.googleapis.com/css2?family=Playfair+Display:wght@400;500;600&display=swap" rel="stylesheet">
<style>
  :root {
    --page: #ffffff;
    --label-blush: #ecdcdc;
    --ink-teal: #14292d;
    --band-teal: #132a2e;
  }
  * { box-sizing: border-box; margin: 0; padding: 0; }
  html, body {
    width: 1200px; height: 1200px; overflow: hidden;
    background: var(--page);
  }
  .canvas {
    width: 1200px; height: 1200px;
    display: flex; align-items: center; justify-content: center;
  }
  .honey-label {
    position: relative;
    width: 540px; height: 920px;
    background: var(--label-blush);
    border-radius: 50% 50% 14% 14% / 26% 26% 7% 7%;
    overflow: hidden;
    font-family: "Playfair Display", serif;
    color: var(--ink-teal);
    text-align: center;
  }
  .brand-mark {
    position: absolute;
    top: 110px; left: 50%;
    transform: translateX(-50%);
    width: 330px; height: 330px;
    border: 1.5px solid var(--ink-teal);
    border-radius: 50%;
    display: flex; align-items: center; justify-content: center;
  }
  .brand-name {
    font-weight: 500;
    font-size: 34px;
    line-height: 1.2;
    letter-spacing: 0.06em;
    text-transform: uppercase;
    color: var(--ink-teal);
  }
  .product-title {
    position: absolute;
    top: 500px; left: 0; right: 0;
  }
  .rule {
    position: relative;
    height: 2px; background: var(--ink-teal);
    margin: 0 auto;
  }
  .rule::before, .rule::after {
    content: ""; position: absolute; top: -3px;
    width: 8px; height: 8px; border-radius: 50%;
    background: var(--ink-teal);
  }
  .rule::before { left: -4px; }
  .rule::after { right: -4px; }
  .rule--top { width: 360px; }
  .rule--bottom { width: 360px; }
  .product-name {
    font-weight: 500;
    font-size: 72px;
    letter-spacing: 0.02em;
    line-height: 1;
    margin: 22px 0 24px;
    white-space: nowrap;
  }
  .address {
    position: absolute;
    top: 700px; left: 0; right: 0;
    font-size: 19px; font-weight: 600;
    line-height: 1.25;
    letter-spacing: 0.03em;
    text-transform: uppercase;
  }
  .net-weight {
    position: absolute;
    top: 785px; left: 0; right: 0;
    font-size: 19px; font-weight: 600;
    letter-spacing: 0.03em;
  }
  .floral-band {
    position: absolute;
    left: 0; right: 0; bottom: 0;
    height: 92px;
    background: linear-gradient(180deg, var(--band-teal), #1a3438);
  }
</style>
</head>
<body>
  <main class="canvas">
    <section class="honey-label">
      <div class="brand-mark">
        <p class="brand-name">Corliss<br>Waverly<br>Botanicals</p>
      </div>

      <div class="product-title">
        <div class="rule rule--top"></div>
        <h1 class="product-name">RAW HONEY</h1>
        <div class="rule rule--bottom"></div>
      </div>

      <p class="address">27308 Quarry Bend Rd<br>Alderbrook, MO 66341</p>
      <p class="net-weight">NET WT. 16 OZ</p>

      <div class="floral-band" role="img" aria-label="Dark teal band with white line-drawn flowers and leaves"></div>
    </section>
  </main>
</body>
</html>
```